Stylist/Barber Standup Sign for Hair Regrowth Company

We want to design an attractive and eye-catching sign for hair stylists and barbers to sit on their workstations to attract the attention of their clients regarding hair loss and encourage them to speak to their stylist about it of they are would like to seek treatment.
50% of men and 25% of women suffer from hair loss but most are in denial that it is happening or too embarrassed to talk about it.

Copy for the flyer is as follows:

[Section 1:]
This flyer has been placed here/designed to spark conversation about hair loss

[Section 2:]
The truth is...
73% of people believe their hair is thinning
They are right

[Section 3:]
If you've got questions, your stylist or barber has answers.

Additional Background Information:

Primary target audience is men between the ages of 25-45, secondary target audience is men 46-60

Current Consumer Perception? (in the first person) “I’ve been thinking about my hair. I think it’s getting thinner and I’m scared, worried and don’t know what to do. But I don’t know if there is anything that really works. I’ve tried other things and nothing‘s worked.”

Tonality of materials? Very guy friendly, matter of fact, authoritative, its what you might hear from your best friend. Confident. Encouraging, but with a sense of urgency.

Please use our brand colors, but do not include our logo or brand name.
Colors are as follows:
Green: #4ca26f
Light Grey: #999999
Dark Grey: #262626

I have attached print templates in both PDF and Jpeg, please use those to provide final ready to print documents if you are selected.

Target Market(s)

Industry/Entity Type

Health And Wellness

Font styles to use
Sans Serif

Colors
00a990
ffffff
333333
cbcbcb

Requirements
Must have
• We want to get across the following messaging. Ideally you will submit a design using our copy and if you think you can do better, please feel free to submit another design with your own copy/messaging. If you can do it better we would love to select you :-)
• Our copy?
• This flyer has been placed here/designed to spark conversation about hair loss
• The truth is...
• 73% of people believe their hair is thinning
• They are right
• If you've got questions, your stylist or barber has answers
• Also please use our brand colors:
• Green: #4ca26f
• Light Grey: #999999
• Dark Grey: #262626
Should not have
• dont add any logos, images or ornate design. this needs to be simple, easy to ready and eye catching.
• do not use the color red in any capacity.

```html
<!DOCTYPE html>
<html lang="en">
<head>
<meta charset="UTF-8">
<title>Hair Loss Conversation Sign</title>
<link rel="stylesheet" href="https://fonts.googleapis.com/css2?family=Figtree:wght@400;800;900&family=Hind:wght@400;600&display=swap">
<style>
  :root {
    --teal: #00a990;
    --white: #ffffff;
    --ink: #333333;
    --band-grey: #cbcbcb;
    --backdrop: #707174;
  }
  * { margin: 0; padding: 0; box-sizing: border-box; }
  html, body {
    width: 1200px;
    height: 1000px;
    overflow: hidden;
    background: var(--backdrop);
  }
  .sign {
    position: absolute;
    left: 310px;
    top: 68px;
    width: 580px;
    height: 862px;
    background: var(--white);
    font-family: "Figtree", "Helvetica Neue", Arial, sans-serif;
    color: var(--ink);
    text-align: center;
  }
  .line {
    position: absolute;
    left: 0;
    width: 100%;
    white-space: nowrap;
  }
  .intro {
    font-size: 27px;
    font-weight: 400;
    line-height: 40px;
  }
  .intro-1 { top: 48px; }
  .intro-2 { top: 88px; }
  .kicker {
    top: 136px;
    font-size: 30px;
    font-weight: 900;
    line-height: 36px;
    color: var(--teal);
    letter-spacing: 0.2px;
  }
  .headline-band {
    position: absolute;
    left: 38px;
    top: 179px;
    width: 503px;
    height: 103px;
    background: var(--teal);
    color: var(--white);
    font-size: 88px;
    font-weight: 900;
    line-height: 103px;
    letter-spacing: 1px;
  }
  .truth {
    font-family: "Hind", "Helvetica Neue", Arial, sans-serif;
    font-weight: 400;
    font-size: 43px;
    line-height: 50px;
  }
  .truth-1 { top: 350px; }
  .truth-2 { top: 405px; }
  .truth-3 { top: 458px; color: var(--teal); }
  .emphasis {
    position: relative;
    font-weight: 600;
  }
  .emphasis::after {
    content: "";
    position: absolute;
    left: 0;
    right: 12px;
    bottom: -8px;
    height: 7px;
    background: var(--teal);
  }
  .verdict-band {
    position: absolute;
    left: 38px;
    top: 535px;
    width: 503px;
    height: 38px;
    background: var(--band-grey);
    font-size: 31px;
    font-weight: 900;
    line-height: 42px;
    color: var(--ink);
  }
  .question {
    top: 658px;
    font-size: 29px;
    font-weight: 400;
    line-height: 36px;
  }
  .advisor {
    top: 697px;
    font-size: 30px;
    font-weight: 900;
    line-height: 36px;
    color: var(--teal);
  }
  .answer {
    top: 740px;
    font-size: 66px;
    font-weight: 900;
    line-height: 66px;
    color: var(--teal);
  }
  .answer-mark {
    position: relative;
  }
  .answer-mark::after {
    content: "";
    position: absolute;
    left: 2px;
    right: -6px;
    bottom: -5px;
    height: 7px;
    background: var(--teal);
  }
</style>
</head>
<body>
  <main class="sign">
    <p class="line intro intro-1">This flyer has been placed here/</p>
    <p class="line intro intro-2">designed to</p>
    <p class="line kicker">SPARK CONVERSATION ABOUT</p>
    <h1 class="headline-band">HAIR LOSS</h1>

    <p class="line truth truth-1">The truth is...</p>
    <p class="line truth truth-2">73% of People Believe</p>
    <p class="line truth truth-3">Their Hair is <span class="emphasis">Thinning</span></p>
    <p class="verdict-band">THEY ARE RIGHT</p>

    <p class="line question">If you've got questions,</p>
    <p class="line advisor">YOUR STYLIST OR BARBER</p>
    <p class="line answer">HAS AN<span class="answer-mark">SWER</span>S.</p>
  </main>
</body>
</html>
```